Real Estate Investor needs awesome business card design

I invest in real estate, focused on multi-family properties, and I need a business card to hand out to potential partners. I prefer simple, clean designs, but it needs to stand out, so I'd like there to be a bit of red in the design as well.

It should include this information:

Front
Calder Whitby
Real Estate Investor
Direct phone: 501-555-0187
Email: calderjwhitby@mailbox-example.net
Headshot (Picture), I've uploaded a few, just pick the one you think looks best with your design. You can remove the background from the headshot image if it looks better.

Back
The back of the card's design should flow and be congruent with the front. On the back I want to put an inspirational quote or question. There will be different ones depending on the card, so I'll need the original file so I can edit it in the end.

For now, use “The Pessimist Sees Difficulty In Every Opportunity. The Optimist Sees The Opportunity In Every Difficulty.” -Edmund Halvorsen

Target Market(s)

Investors

Industry/Entity Type

Real Estate

Contact Information for Business Card

Front
Calder Whitby
Real Estate Investor

Back
The back of the card's design should flow and be congruent with the front. On the back I want to put an inspirational quote or question. There will be different ones depending on the card, so I'll need the original file so I can edit it in the end. I've uploaded some EXAMPLES of business cards with quotes on them. Don't copy but feel free to use them as inspiration.

The design will be printed on "ZAP sized" business cards
1039 x 697 pixels
with rounded corners

Font styles to use
Serif
Decorative
Script

Colors
ec1f27

Requirements
Must have
• Headshot, name, and other information in it.
• 1039 x 697 pixels
• Rounded corners
• Clean design that pops. I'm open to see any color background, including black.
• Headshots can be located here: https://www.filecrate-example.com/sh/8kx2vq71ld0pa3z/BQQTXL7mrrf9eT3Kq0HhgkLm2b?dl=0
Nice to have
• It would be awesome if the design included a personal signature or monogram, but if not I'll get a personal logo developed later and the card redesigned if I think it needs it.
Should not have
• Cluttered design

```html
<!DOCTYPE html>
<html lang="en">
<head>
<meta charset="utf-8">
<title>Calder Whitby — Business Card</title>
<link rel="stylesheet" href="https://fonts.googleapis.com/css2?family=Bitter:wght@400;600;700&family=Mulish:wght@400;800&display=swap">
<style>
  :root {
    --red: #ec1f27;
    --ink: #141414;
    --quote-grey: #b4b4b4;
    --soft-grey: #b9b9b9;
    --title-grey: #6a6a6a;
    --paper: #ffffff;
    --backdrop: #262626;
    --photo-dark: #1b1b1b;
    --photo-mid: #4a4a4a;
  }
  * { box-sizing: border-box; margin: 0; padding: 0; }
  html, body { width: 1200px; height: 900px; overflow: hidden; }
  body { background: var(--backdrop); position: relative; }

  .card {
    position: absolute;
    width: 560px;
    height: 376px;
    background: var(--paper);
    border-radius: 28px;
    overflow: hidden;
  }

  /* Back: quote */
  .card--back { left: 110px; top: 50px; }
  .quote {
    position: absolute;
    left: 58px;
    top: 96px;
    width: 460px;
    font-family: "Mulish", sans-serif;
    font-weight: 800;
    font-size: 25px;
    line-height: 1.2;
    letter-spacing: 0.04em;
    color: var(--ink);
    text-transform: uppercase;
  }
  .quote__muted { color: var(--quote-grey); }
  .quote__author {
    position: absolute;
    left: 60px;
    top: 258px;
    font-family: "Mulish", sans-serif;
    font-weight: 400;
    font-size: 12px;
    letter-spacing: 0.05em;
    color: var(--soft-grey);
    text-transform: uppercase;
  }

  /* Front: contact */
  .card--front { left: 530px; top: 474px; }
  .band { position: absolute; left: 0; width: 100%; background: var(--red); }
  .band--top { top: 0; height: 26px; }
  .band--bottom { bottom: 0; height: 20px; }
  .headshot {
    position: absolute;
    right: 0;
    top: 26px;
    bottom: 62px;
    width: 268px;
    background: radial-gradient(ellipse at 55% 40%, var(--photo-mid), var(--photo-dark) 70%);
  }
  .band--lower { bottom: 42px; height: 20px; right: 0; width: 268px; left: auto; }
  .identity { position: absolute; left: 32px; top: 56px; }
  .identity__name {
    font-family: "Bitter", serif;
    font-weight: 700;
    font-size: 34px;
    color: var(--red);
    line-height: 1;
  }
  .identity__title {
    font-family: "Bitter", serif;
    font-weight: 600;
    font-size: 15px;
    color: var(--title-grey);
    letter-spacing: 0.02em;
    margin-top: 6px;
  }
  .contact {
    position: absolute;
    left: 32px;
    bottom: 44px;
    font-family: "Bitter", serif;
    font-size: 13px;
    color: var(--title-grey);
    line-height: 1.55;
  }
  .contact__label { color: var(--red); font-weight: 600; }
</style>
</head>
<body>
  <section class="card card--back" aria-label="Card back">
    <p class="quote">"<span class="quote__muted">The pessimist</span> sees difficulty in every oppertunity. <span class="quote__muted">The optimist</span> sees the oppertunity in every difficulty."</p>
    <p class="quote__author">-Edmund Halvorsen.</p>
  </section>

  <section class="card card--front" aria-label="Card front">
    <div class="band band--top"></div>
    <div class="headshot" role="img" aria-label="Black and white headshot of Calder Whitby in a dark suit"></div>
    <div class="band band--lower"></div>
    <div class="band band--bottom"></div>
    <div class="identity">
      <h1 class="identity__name">Calder Whitby</h1>
      <p class="identity__title">REAL ESTATE INVESTOR</p>
    </div>
    <div class="contact">
      <p><span class="contact__label">P-</span> 501-555-0187</p>
      <p><span class="contact__label">E-</span> calderjwhitby@mailbox-example.net</p>
    </div>
  </section>
</body>
</html>
```